Flyer for Makeup Class

A flyer for my makeup class promotion. I am a make up artist starting a group class to teach makeup to ladies. I have attached some verbiage handwritten. My picture is the one in pink hijab. I have also attached some inspiration ideas and color combination (the colors in the cake design are the ones I want to use).

Target Market(s)

Ladies looking to learn make up from a make up artist

Industry/Entity Type

Hair And Beauty

Requirements
Must have
• The verbiage / description that I have hand written should be written using graphics and nice fonts. You can change the exact wording to make it better.

```html
<!DOCTYPE html>
<html lang="en">
<head>
<meta charset="utf-8">
<title>Exclusive Makeup Masterclass Flyer</title>
<link href="https://fonts.googleapis.com/css2?family=Kaushan+Script&family=Roboto:ital,wght@0,400;0,500;0,700;1,500&display=swap" rel="stylesheet">
<style>
:root{
  --page:#e2e2e2;
  --paper:#f2f1ef;
  --frame:#b56a6a;
  --wine:#8a2c2c;
  --olive:#6b4a1f;
  --band:#a9302a;
  --ink:#2a2a2a;
  --tint:#f7ebe3;
  --pink:#d9577f;
  --rose:#e98aa7;
}
*{margin:0;padding:0;box-sizing:border-box}
html,body{width:1200px;height:1200px;overflow:hidden;background:var(--page)}
.flyer{position:absolute;left:194px;top:30px;width:729px;height:1023px;transform:scale(1.114);transform-origin:0 0;background:var(--paper);overflow:hidden;font-family:"Roboto",sans-serif;color:var(--ink)}
.frame{position:absolute;left:22px;top:22px;width:686px;height:980px;border:2px solid var(--frame);opacity:.8}
.art{position:absolute}
.portrait{left:0;top:60px;width:365px;height:392px;background:linear-gradient(180deg,#f7f0ee 0%,#f5cdc3 45%,#f3b3aa 75%,#e4208f 100%);border-radius:180px 180px 0 0}
.brushes{left:272px;top:0;width:290px;height:180px;background:linear-gradient(160deg,#2c2c2c 0%,#4a4a4a 55%,#d6306e 100%);border-radius:0 0 120px 40px}
.powder-heart{left:512px;top:0;width:217px;height:205px;background:radial-gradient(circle at 55% 45%,#f0a3b8 0%,#e57b98 55%,rgba(229,123,152,0) 75%)}
.blush{left:0;top:640px;width:185px;height:383px;background:radial-gradient(ellipse at 30% 55%,#c54a78 0%,#d2668e 50%,rgba(210,102,142,0) 78%)}
.jar{left:520px;top:890px;width:209px;height:133px;background:radial-gradient(ellipse at 40% 60%,#e9c4b8 0%,#d8b0a8 40%,rgba(216,176,168,0) 70%),linear-gradient(135deg,rgba(0,0,0,0) 60%,#1d1d1d 61%)}
.title{position:absolute;font-family:"Kaushan Script",cursive;color:var(--wine);text-align:center;white-space:nowrap}
.title-main{left:330px;top:208px;width:360px;font-size:70px}
.title-sub{left:330px;top:294px;width:370px;font-size:40px}
.title-by{left:470px;top:356px;width:140px;font-size:80px;color:var(--olive)}
.name-band{position:absolute;left:0;top:451px;width:395px;height:71px;background:var(--band);color:#fff;text-align:center;padding-top:6px}
.name-band .name{font-size:26px;font-weight:700;line-height:32px}
.name-band .role{font-size:19px;line-height:24px}
.venue{position:absolute;left:43px;top:550px;width:643px;height:50px;border:1.5px solid var(--frame);font-size:28px;font-weight:500;text-align:center;line-height:47px}
.date{position:absolute;left:0;top:620px;width:729px;text-align:center;font-size:33px;font-weight:500;padding-left:10px}
.date sup{font-size:18px}
.audience{position:absolute;left:221px;top:687px;width:487px;height:70px;background:var(--tint);border:1.5px solid var(--frame);font-size:23px;font-style:italic;font-weight:500;line-height:29px;padding:5px 0 0 17px}
.details{position:absolute;left:220px;top:783px;width:480px;font-size:15px;line-height:19px}
.book{position:absolute;left:219px;top:839px;font-size:23px;font-style:italic;font-weight:700;letter-spacing:.2px}
.phones{position:absolute;left:220px;top:880px;font-size:24px;font-weight:500;display:flex;gap:12px;align-items:center}
.phones span{display:flex;align-items:center;gap:6px}
.social{position:absolute;left:220px;top:918px;font-size:18px;display:flex;align-items:center;gap:9px}
.social i{display:block;width:19px;height:19px;border-radius:50%;background:var(--ink)}
</style>
</head>
<body>
<div class="flyer">
  <div class="frame"></div>
  <div class="art portrait" role="img" aria-label="Portrait of the makeup artist in a pink hijab"></div>
  <div class="art brushes" role="img" aria-label="Makeup brushes with pink powder"></div>
  <div class="art powder-heart" role="img" aria-label="Pink powder with a heart drawn in it"></div>
  <div class="art blush" role="img" aria-label="Crushed pink blush"></div>
  <div class="art jar" role="img" aria-label="Pot of highlighter with its box"></div>

  <h1 class="title title-main">Exclusive</h1>
  <div class="title title-sub">Mackup Masterclass</div>
  <div class="title title-by">By</div>

  <div class="name-band">
    <div class="name">ZARA MALIK</div>
    <div class="role">(UK Based Mua)</div>
  </div>

  <div class="venue">Venue: Rosewood Garden Hall(Islamabad)</div>
  <div class="date">6<sup>th</sup> April 2019 | 11:30 - 5:30 pm</div>

  <div class="audience">Perfect for Professionals, Begginners<br>and make up lovers</div>

  <p class="details">This Class is packed with loads information tips, live demos, goodie Bag, Certificate, Q&amp;A, lunch and much more .....</p>

  <div class="book">TO BOOK YOU PLACE, CONTACT</div>
  <div class="phones">
    <span><svg width="20" height="20" viewBox="0 0 20 20"><circle cx="10" cy="10" r="10" fill="#1d1d1d"/><path d="M6.5 5.5c.6-.5 1.2-.4 1.5.1l1 1.6c.2.4.1.8-.2 1.1l-.6.5c.5 1.2 1.5 2.2 2.7 2.7l.5-.6c.3-.3.7-.4 1.1-.2l1.6 1c.5.3.6.9.1 1.5-.8.9-2 1-3.3.3-2-1-3.5-2.5-4.5-4.5-.6-1.3-.5-2.5.1-3.5z" fill="#fff"/></svg>0770123456</span>
    <span><svg width="20" height="20" viewBox="0 0 20 20"><circle cx="10" cy="10" r="10" fill="#1d1d1d"/><path d="M6.5 5.5c.6-.5 1.2-.4 1.5.1l1 1.6c.2.4.1.8-.2 1.1l-.6.5c.5 1.2 1.5 2.2 2.7 2.7l.5-.6c.3-.3.7-.4 1.1-.2l1.6 1c.5.3.6.9.1 1.5-.8.9-2 1-3.3.3-2-1-3.5-2.5-4.5-4.5-.6-1.3-.5-2.5.1-3.5z" fill="#fff"/></svg>03001234567</span>
  </div>
  <div class="social"><i></i>zaramalikstudio</div>
</div>
</body>
</html>
```